Hip Surgeon needs a web page re-design.

I have a web page to provide information about the diseases of the hip joint for the patients from my private practice since 2008. I need a re-design job for a fresh new look.
We have made a new logo and a new stationery design here in CraftLoomery (please see the uploaded files) and I want to make my web page look-alike the new design concepts.
I like the color blue and tones of blue, matching my logo and stationery.
I don't like "busy" designs. It must be clean, elegant and ease to read. The final design should be "mobile friendly" if possible.
Please visit my website www.pontevivaclinica.com.br to take a look and get some inspiration.

```html
<!DOCTYPE html>
<html lang="pt-BR">
<head>
<meta charset="utf-8">
<title>Dr. Rafael M. Correa — Cirurgia do Quadril</title>
<link rel="stylesheet" href="https://fonts.googleapis.com/css2?family=Arimo:wght@400;700&family=Roboto+Condensed:wght@400&display=swap">
<style>
  :root {
    --bar: #3a3a3a;
    --brand: #2a9fe6;
    --sky-top: #82d3fb;
    --sky-bottom: #0388ff;
    --page: #f4f4f4;
    --ink: #141414;
    --name-red: #c8101a;
    --nav-teal: #2fb3b1;
    --nav-green: #3aa63a;
    --muted: #a9a9a9;
  }
  * { margin: 0; padding: 0; box-sizing: border-box; }
  html, body { width: 1200px; height: 960px; overflow: hidden; }
  body { background: var(--page); font-family: "Arimo", Arial, sans-serif; color: var(--ink); position: relative; }

  .site-header { position: absolute; left: 0; top: 0; width: 1200px; height: 124px; background: var(--bar); }
  .brand { position: absolute; left: 111px; top: 23px; display: flex; align-items: center; gap: 14px; }
  .brand-mark { width: 82px; height: 82px; border-radius: 50%; background: var(--brand); }
  .brand-name { font-family: "Roboto Condensed", Arial, sans-serif; font-size: 38px; color: var(--brand); letter-spacing: -0.5px; }

  .main-nav a { position: absolute; text-decoration: none; font-family: "Arimo", Arial, sans-serif; font-weight: 700; font-size: 21px; letter-spacing: 5px; line-height: 28px; }
  .nav-home { left: 570px; top: 70px; width: 110px; height: 28px; text-align: center; background: linear-gradient(#5fd6d2, var(--nav-teal) 55%, #1c8785); color: #06262a; border-radius: 3px; box-shadow: 0 2px 3px rgba(0,0,0,.5); }
  .nav-about { left: 708px; top: 71px; color: #0c3a46; text-shadow: 0 0 4px #4ac7d6, 0 0 2px #4ac7d6; }
  .nav-contact { left: 1032px; top: 74px; color: #0f2e0f; text-shadow: 0 0 4px var(--nav-green), 0 0 2px var(--nav-green); }

  .intro-band { position: absolute; left: 0; top: 124px; width: 1200px; height: 270px; background: linear-gradient(var(--sky-top), var(--sky-bottom)); box-shadow: 0 4px 6px rgba(0,0,0,.25); }
  .portrait-frame { position: absolute; left: 165px; top: 143px; width: 164px; height: 231px; background: #fff; padding: 5px 8px 10px 5px; box-shadow: 0 1px 3px rgba(0,0,0,.2); }
  .portrait { width: 100%; height: 100%; background: linear-gradient(160deg, #cfc6bb 0%, #e9e9ea 45%, #f6f7f9 100%); box-shadow: 0 2px 4px rgba(0,0,0,.35); }
  .doctor-name { position: absolute; left: 504px; top: 146px; font-size: 23px; font-weight: 700; color: var(--name-red); letter-spacing: 5.2px; }
  .intro-text { position: absolute; left: 503px; top: 202px; width: 600px; font-size: 16.5px; line-height: 20.3px; letter-spacing: 3.6px; }
  .intro-text p + p { margin-top: 20px; }

  .content { position: absolute; left: 108px; top: 461px; width: 1000px; font-size: 16.5px; line-height: 20.3px; letter-spacing: 3.9px; }
  .content p + p { margin-top: 20.3px; }

  .site-footer { position: absolute; left: 0; top: 896px; width: 1200px; height: 64px; background: var(--bar); }
  .footer-brand { position: absolute; left: 111px; top: 12px; display: flex; align-items: center; gap: 8px; }
  .footer-mark { width: 42px; height: 42px; border-radius: 50%; background: #8c8c8c; }
  .footer-name { font-family: "Roboto Condensed", Arial, sans-serif; font-size: 20px; color: var(--muted); }
  .copyright { position: absolute; left: 365px; top: 32px; font-family: "Roboto Condensed", Arial, sans-serif; font-size: 12px; letter-spacing: 2.6px; color: var(--muted); }
</style>
</head>
<body>
  <header class="site-header">
    <div class="brand">
      <span class="brand-mark"></span>
      <span class="brand-name">Dr. Rafael M. Correa</span>
    </div>
    <nav class="main-nav">
      <a class="nav-home" href="#">Home</a>
      <a class="nav-about" href="#">Saiba Mais</a>
      <a class="nav-contact" href="#">Contato</a>
    </nav>
  </header>

  <section class="intro-band"></section>
  <div class="portrait-frame">
    <div class="portrait" role="img" aria-label="Retrato do médico de jaleco branco"></div>
  </div>
  <h1 class="doctor-name">Dr. Rafael Moreira Correa</h1>
  <div class="intro-text">
    <p>Seja bem vindo ao site “Ponte Viva”!</p>
    <p>O objetivo deste site é fornecer ao público leigo informações sobre as principais doenças e procedimentos cirúrgicos envolvendo o quadril e a pelve, como próteses de quadril, artroscopia (cirurgia por vídeo), etc.</p>
  </div>

  <main class="content">
    <p>Idealizei este site e realizei todos os esforços de maneira a disponibilizar a você conhecimentos atualizados de fontes confiáveis, como livros texto e publicações científicas nacionais e estrangeiras. Incluí também as últimas conquistas em nossa área, filtrando estas informações e “traduzindo-as” de modo que a pessoa que não é familiarizada com o jargão médico possa entendê-la da melhor maneira possível.</p>
    <p>A internet é uma ferramenta que a cada dia é mais utilizada para busca de informações referentes à saúde. Devido à sua natureza amplamente livre as informações existentes em alguns sites podem conter inexatidões ou mesmo informações tendenciosas que podem gerar dúvidas ou expectativas irreais.</p>
    <p>Ressalto que o material contido neste site é um suporte estritamente informativo, de maneira nenhuma deve ser tomado com finalidade diagnóstica ou substituir uma consulta médica!</p>
    <p>Sinta-se à vontade para enviar seus comentários, críticas, perguntas ou obter outras informações através do link “Contato”.</p>
  </main>

  <footer class="site-footer">
    <div class="footer-brand">
      <span class="footer-mark"></span>
      <span class="footer-name">Dr. Rafael M. Correa</span>
    </div>
    <p class="copyright">© 2014 All rights reserved</p>
  </footer>
</body>
</html>
```